Still and Animated Adult Banner Ad Design

Looking for Adult Banner Ad Designs for velvetmarigold.com The banner ads must be stylish, and be able to stand out in a very crowded market place.
Have a look at brisknode.co.uk to get an idea of how crowded this space can be. Will need designs for landscape / profile, and different sizes.
I've attached images which you can use to help with the design but you can also add images yourself if you think it will help the design.
For skinny horizontal images, just use the brand name VELVET MARIGOLD
Ideally I need access to parts used in design with .png transparency, so later I can edit and make myself using the parts, as there are many size dimensions needed.
1000 x 130
163 x 325
140 x 140
1000 x 1000
270 x 400
468 x 60
160 x 60
468 x 60
736 x 80
600 x 400
20 x 220
Images need to use lowest resolution to be uploaded to these websites.
486 x 60 with logo image with the following text:
Recruiting Now
300 X 450
Recruiting Escorts and Masseuses
Independents Welcome
Training Provided

```html
<!DOCTYPE html>
<html lang="en">
<head>
<meta charset="utf-8">
<title>Velvet Marigold — Recruitment Banners</title>
<link href="https://fonts.googleapis.com/css2?family=Poppins:wght@400;600&display=swap" rel="stylesheet">
<style>
  :root {
    --stage-centre: #5e5e5e;
    --stage-edge: #2f2f2f;
    --banner-dark: #15110f;
    --pink: #f7286a;
    --pink-soft: #ff6b93;
    --white: #ffffff;
    --brand-gold: #8c6a3c;
    --band-text: #7a5020;
    --label: #f2f2f2;
  }
  * { box-sizing: border-box; margin: 0; padding: 0; }
  html, body { width: 1200px; height: 1200px; overflow: hidden; }
  body {
    position: relative;
    font-family: "Poppins", sans-serif;
    background: radial-gradient(circle at 50% 40%, var(--stage-centre) 0%, var(--stage-edge) 75%);
  }
  .size-label {
    position: absolute;
    left: 0; width: 1200px;
    text-align: center;
    color: var(--label);
    font-size: 20px;
    font-weight: 400;
    letter-spacing: 0.5px;
  }
  .size-label--portrait { top: 153px; }
  .size-label--leaderboard { top: 867px; }

  .banner {
    position: absolute;
    overflow: hidden;
    background: var(--banner-dark);
    box-shadow: 0 10px 40px rgba(0,0,0,0.45);
  }
  .banner--portrait { left: 400px; top: 195px; width: 400px; height: 600px; }
  .banner--leaderboard { left: 288px; top: 911px; width: 624px; height: 80px; }

  .photo {
    position: absolute;
    background:
      radial-gradient(ellipse at 50% 45%, #c99778 0%, #8a5a42 30%, rgba(40,26,20,0) 65%),
      linear-gradient(180deg, #1e1713, #120e0c);
  }
  .banner--portrait .photo { left: 0; top: 0; width: 400px; height: 600px; }
  .banner--leaderboard .photo {
    left: 172px; top: 0; width: 107px; height: 80px;
    background: radial-gradient(ellipse at 50% 50%, #c7a070 0%, #7c5a3c 45%, #1a1410 90%);
  }

  .brand-name {
    position: absolute;
    color: var(--brand-gold);
    font-weight: 400;
    text-align: center;
    line-height: 1.15;
    text-transform: uppercase;
  }
  .brand-name__dot {
    display: block;
    margin: 0 auto 8px;
    border-radius: 50%;
    border: 2px solid var(--brand-gold);
  }
  .banner--portrait .brand-name { right: 14px; top: 28px; width: 118px; font-size: 17px; letter-spacing: 1px; }
  .banner--portrait .brand-name__dot { width: 34px; height: 34px; }
  .banner--leaderboard .brand-name { left: 14px; top: 10px; width: 118px; font-size: 12px; letter-spacing: 0.5px; }
  .banner--leaderboard .brand-name__dot { width: 20px; height: 20px; margin-bottom: 4px; }

  .heart { position: absolute; left: 0; top: 0; }

  .offer {
    position: absolute;
    left: 0; width: 400px;
    text-align: center;
  }
  .offer__headline {
    top: 413px;
    color: var(--white);
    font-size: 30px;
    line-height: 1.1;
  }
  .offer__band {
    top: 496px; height: 52px;
    background: var(--white);
    color: var(--band-text);
    font-size: 28px;
    line-height: 52px;
  }
  .offer__note {
    top: 550px;
    color: var(--white);
    font-size: 28px;
    line-height: 46px;
  }

  .cta {
    position: absolute;
    left: 344px; width: 252px; top: 38px;
    text-align: center;
    color: var(--white);
    font-weight: 600;
    font-size: 20px;
    line-height: 30px;
    text-transform: uppercase;
  }
</style>
</head>
<body>

  <div class="size-label size-label--portrait">300 X 450</div>

  <section class="banner banner--portrait">
    <div class="photo" role="img" aria-label="Photo of a blonde model in black lace lingerie against a dark studio background"></div>

    <div class="brand-name">
      <span class="brand-name__dot"></span>
      Velvet<br>Marigold
    </div>

    <svg class="heart" width="400" height="600" viewBox="0 0 400 600" aria-hidden="true">
      <path d="M200,405 C200,370 150,353 93,353 C28,353 -22,400 -22,472 C-22,565 120,650 200,730 C280,650 422,565 422,472 C422,400 372,353 307,353 C250,353 200,370 200,405 Z"
            fill="var(--pink)" stroke="var(--white)" stroke-width="4"/>
      <path d="M200,520 C200,495 170,485 140,485 C105,485 80,510 80,545 C80,590 150,620 200,660 C250,620 320,590 320,545 C320,510 295,485 260,485 C230,485 200,495 200,520 Z"
            fill="var(--pink-soft)" opacity="0.35"/>
    </svg>

    <p class="offer offer__headline">Recruiting Escorts and<br>Masseuses</p>
    <p class="offer offer__band">Independents Welcome</p>
    <p class="offer offer__note">Training Provided</p>
  </section>

  <div class="size-label size-label--leaderboard">486 X 60</div>

  <section class="banner banner--leaderboard">
    <div class="brand-name">
      <span class="brand-name__dot"></span>
      Velvet Marigold
    </div>

    <div class="photo" role="img" aria-label="Cropped photo of a blonde model's face"></div>

    <svg class="heart" width="624" height="80" viewBox="0 0 624 80" aria-hidden="true">
      <path d="M470,30 C470,12 440,1 407,1 C370,1 344,28 344,66 C344,110 420,150 470,190 C520,150 596,110 596,66 C596,28 570,1 533,1 C500,1 470,12 470,30 Z"
            fill="var(--pink)" stroke="var(--white)" stroke-width="3"/>
      <ellipse cx="470" cy="58" rx="42" ry="26" fill="var(--pink-soft)" opacity="0.35"/>
    </svg>

    <p class="cta">Recruiting Now</p>
  </section>

</body>
</html>
```